Quillon Maison Wood Fired Pizza business card design

I have a logo and need an eye catching design that will get me noticed.
My business is wood fired pizza. I want a bold design that will make our customers remember us and the food that we serve. Work with the colors of our logo and texts. Maybe add designs that lend to what or how pizza is made using our wood fired oven?

Target Market(s)

Foodies!

Contact Information for Business Card

Quillon Maison Wood Fired Pizza
Our slogan is Fast. Fresh. Handcrafted
Catering for all events

Requirements
Must have
• Dana Porrick
Telephone 570 555 0183
website www.getquillon.example
Facebook @getquillonpizza maybe use the facebook logo next to it
Instagram getquillonpizza maybe use the instagram logo next to it
Catering for all events
Nice to have
• Maybe pizza peels, pizza cutters? Wood? Fired wood? Using our flame in the background?
Please work with different colored text so each sentence stands out? A themed color for facebook?
Maybe work with the colors within our logo?
Please try to use the our quillon font, but not a must have.

```html
<!DOCTYPE html>
<html lang="en">
<head>
<meta charset="utf-8">
<title>Quillon Maison Wood Fired Pizza – Business Card</title>
<link href="https://fonts.googleapis.com/css2?family=Bebas+Neue&family=Roboto:wght@400;700&display=swap" rel="stylesheet">
<style>
  :root {
    --backdrop: #a3a3a3;
    --ink: #13161f;
    --flame-red: #cc0e13;
    --ember-orange: #f0951f;
    --paper: #ffffff;
    --dot-blue: #4a6fb5;
    --dot-pink: #d6336c;
  }
  * { box-sizing: border-box; margin: 0; padding: 0; }
  html, body { width: 1200px; height: 1200px; overflow: hidden; }
  body { background: var(--backdrop); position: relative; font-family: "Roboto", Arial, sans-serif; }

  .card { position: absolute; top: 303px; width: 370px; height: 594px; overflow: hidden; }

  /* Front: slogan side */
  .card-front { left: 200px; background: var(--flame-red); }
  .flame-artwork {
    position: absolute; inset: 0 0 190px 0;
    background: linear-gradient(180deg, var(--ink) 0%, var(--ink) 35%, var(--flame-red) 100%);
  }
  .slogan {
    position: absolute; left: 0; right: 0; top: 456px;
    font-family: "Bebas Neue", Impact, sans-serif; color: var(--paper);
    font-size: 38px; line-height: 49px; text-align: center;
  }

  /* Back: contact side */
  .card-back { left: 599px; width: 365px; background: var(--paper); text-align: center; color: var(--ink); }
  .brand-mark {
    position: absolute; left: 50%; top: 55px; width: 150px; height: 150px;
    margin-left: -75px; border-radius: 50%; background: var(--flame-red);
  }
  .brand-name {
    position: absolute; left: 0; right: 0; top: 262px;
    font-weight: 700; font-size: 28px; letter-spacing: 3px; color: var(--ink);
  }
  .person-name {
    position: absolute; left: 0; right: 0; top: 384px;
    font-weight: 700; font-size: 26px; color: var(--flame-red);
  }
  .name-rule {
    position: absolute; left: 50%; top: 421px; width: 148px; margin-left: -74px;
    border-top: 1px solid var(--ember-orange);
  }
  .contact { position: absolute; left: 0; right: 0; top: 431px; font-size: 17px; line-height: 22px; }
  .social-row {
    position: absolute; left: 0; right: 0; top: 490px;
    display: flex; align-items: center; justify-content: center; gap: 5px;
  }
  .social-rule { width: 42px; border-top: 1px solid var(--ember-orange); }
  .social-rule.left { margin-right: 5px; }
  .social-rule.right { margin-left: 5px; }
  .social-dot { width: 24px; height: 24px; border-radius: 50%; }
  .social-dot.first { background: var(--dot-blue); }
  .social-dot.second { background: var(--dot-pink); }
  .handles { position: absolute; left: 0; right: 0; top: 517px; font-size: 17px; line-height: 22px; }
</style>
</head>
<body>
  <section class="card card-front">
    <div class="flame-artwork" role="img" aria-label="Large red flame illustration on a dark background"></div>
    <p class="slogan">Fast. Fresh. Handcrafted<br>Catering for all events</p>
  </section>

  <section class="card card-back">
    <div class="brand-mark"></div>
    <h1 class="brand-name">QUILLON MAISON</h1>
    <h2 class="person-name">DANA PORRICK</h2>
    <div class="name-rule"></div>
    <p class="contact">570 555 0183<br>www.getquillon.example</p>
    <div class="social-row">
      <span class="social-rule left"></span>
      <span class="social-dot first"></span>
      <span class="social-dot second"></span>
      <span class="social-rule right"></span>
    </div>
    <p class="handles">@getquillonpizza<br>getquillonpizza</p>
  </section>
</body>
</html>
```